ターゲットは、墓地を探している方です。生前墓、小規模墓地、ペットと共に墓地に入れる敷地も用意されています。
http://www.asahidaireien.jp/
1ページ
緑 青
• イラストレーター形式 (.ai)
サイトレイアウトのPDFデータです。

弊社お客様にデザインを選んでいただきました。
お客様のイメージと一致したようでとても喜んでいただきました。

すばらしいデザインをありがとうございました。
24デザインの中からお客様に選んでいただきました。
お客様はとても喜んでおります。
今後ともよろしくお願いします。

```html
<!DOCTYPE html>
<html lang="ja">
<head>
<meta charset="utf-8">
<title>朝日台霊園</title>
<link href="https://fonts.googleapis.com/css2?family=Noto+Sans+JP:wght@400;700&family=Noto+Serif+JP:wght@500;700&display=swap" rel="stylesheet">
<style>
:root{
  --green-dark:#1f4a2c;
  --green:#3f7a46;
  --green-light:#8fb58c;
  --bg:#eef1ec;
  --panel:#ffffff;
  --text:#444;
  --line:#d6ddd3;
  --sky:#b9cfdc;
}
*{box-sizing:border-box;margin:0;padding:0}
html,body{width:1200px;height:2200px;overflow:hidden}
body{background:var(--bg);font-family:"Noto Sans JP",sans-serif;color:var(--text);font-size:13px;line-height:1.9;position:relative}
.header{height:100px;background:linear-gradient(#fbfcf9,#eef2ea);display:flex;align-items:center;justify-content:space-between;padding:0 60px}
.brand{display:flex;align-items:center;gap:18px}
.brand-mark{width:40px;height:40px;background:var(--green)}
.brand-name{font-family:"Noto Serif JP",serif;font-weight:700;font-size:36px;color:var(--green-dark);letter-spacing:4px}
.tel{display:flex;align-items:center;gap:10px;border:1px solid var(--line);background:#fff;padding:8px 18px}
.tel-label{font-size:12px;color:#666}
.tel-num{font-size:28px;font-weight:700;color:var(--green-dark);letter-spacing:1px}
.nav{height:30px;background:var(--green-dark);display:flex;justify-content:center}
.nav a{color:#fff;text-decoration:none;font-size:13px;padding:0 26px;line-height:30px;border-right:1px solid rgba(255,255,255,.2)}
.hero{height:250px;background:linear-gradient(180deg,#dfe9ef 0%,#a9c3a0 55%,#6f8f6a 75%,#9a9c96 100%)}
.wrap{position:absolute;top:440px;left:100px;width:1000px;display:flex;gap:24px}
.main{width:720px}
.side{width:256px}
.panel{background:var(--panel);border:1px solid var(--line);padding:24px 30px;margin-bottom:30px}
.h2{font-family:"Noto Serif JP",serif;font-size:20px;color:var(--green-dark);border-left:6px solid var(--green);padding-left:14px;margin-bottom:18px;border-bottom:1px solid var(--line);padding-bottom:6px}
.panel p{margin-bottom:12px}
.video{width:420px;height:250px;margin:20px auto 6px;background:#222;position:relative;border:1px solid #999}
.video-shot{position:absolute;inset:30px 0 30px 0;background:linear-gradient(#cbd8df,#8a9a87 60%,#707070)}
.video-title{position:absolute;top:6px;left:10px;color:#fff;font-size:12px}
.play{position:absolute;left:185px;top:100px}
.topic{display:flex;gap:30px;border-bottom:1px dotted var(--line);padding:6px 0}
.side-box{background:#fff;border:1px solid var(--line);margin-bottom:24px}
.side-h{background:var(--green);color:#fff;font-weight:700;padding:6px 14px;font-size:14px}
.side-list li{list-style:none;border-bottom:1px dotted var(--line);padding:8px 14px;font-size:12px}
.scene{display:flex;gap:10px;align-items:center;padding:8px 12px;border-bottom:1px dotted var(--line);font-size:12px}
.thumb{width:70px;height:48px;background:linear-gradient(#c7d6c2,#7f9a7b)}
.access-photo{height:90px;margin:12px;background:linear-gradient(#cfdce4,#8ea889 70%,#a0a09a)}
.access-text{padding:0 12px 10px;font-size:11.5px;line-height:1.8}
.map{height:110px;margin:0 12px 10px;background:#e4e6df;position:relative;border:1px solid var(--line)}
.footer{position:absolute;left:0;top:2010px;width:1200px;height:190px;background:var(--green-dark);color:#dfe8dc;padding:30px 100px;display:flex;justify-content:space-between}
.footer .brand-name{color:#fff;font-size:26px}
.footer .brand-mark{width:28px;height:28px;background:#fff}
.f-addr{font-size:11px;margin-top:10px;line-height:1.8}
.f-links{font-size:11px;text-align:right}
.copy{position:absolute;bottom:14px;left:100px;font-size:10px;color:#a9bba6}
</style>
</head>
<body>
<header class="header">
  <div class="brand"><div class="brand-mark"></div><div class="brand-name">朝日台霊園</div></div>
  <div class="tel">
    <svg width="22" height="22" viewBox="0 0 24 24"><path d="M6 2h4l2 5-3 2a11 11 0 0 0 6 6l2-3 5 2v4a2 2 0 0 1-2 2A18 18 0 0 1 4 4a2 2 0 0 1 2-2z" fill="#3f7a46"/></svg>
    <span class="tel-label">お問合せ</span><span class="tel-num">0120-48-2631</span>
  </div>
</header>
<nav class="nav"><a>ホーム</a><a>朝日台霊園の紹介</a><a>墓所・サイズ</a><a>墓地マップ</a><a>お申込みの方</a><a>資料請求</a><a>お問合せ</a></nav>
<div class="hero" role="img" aria-label="青空の下に広がる霊園の墓石と緑の木々の風景写真"></div>

<div class="wrap">
  <main class="main">
    <section class="panel">
      <h2 class="h2">朝日台霊園について</h2>
      <p>緑と青空に包まれた朝日台の丘に、穏やかな時間が流れる霊園です。</p>
      <p>生前墓から小規模墓地まで、ご家族の想いに合わせたお墓をご用意しております。</p>
      <p>区画は（約1.0㎡～4.0㎡）をご用意しております。</p>
      <p>宗旨・宗派を問わず、どなたでもご利用いただけます。</p>
      <p>ペットと一緒に眠れる専用の区画も設けております。</p>
      <p>管理事務所にはスタッフが常駐し、清掃と管理を行っております。</p>
      <p>見学はいつでも承っております。お気軽にお問合せください。</p>
      <p>ご案内の様子を動画でもご覧いただけます。</p>
      <div class="video">
        <div class="video-title">朝日台霊園のご案内</div>
        <div class="video-shot" role="img" aria-label="霊園の墓所を映した動画の場面"></div>
        <svg class="play" width="50" height="36" viewBox="0 0 50 36"><rect width="50" height="36" rx="8" fill="#222" opacity=".85"/><path d="M20 10l12 8-12 8z" fill="#fff"/></svg>
      </div>
    </section>

    <section class="panel">
      <h2 class="h2">霊園について</h2>
      <p>霊園の区画・霊園の設備・霊園の管理・霊園の区画・霊園の設備・霊園の管理・霊園の区画・霊園の設備・霊園の管理・霊園の区画・霊園の設備・霊園の管理・霊園の区画・霊園の設備・霊園の管理・霊園の区画・霊園の設備・霊園の管理。</p>
      <p>霊園の区画・霊園の設備・霊園の管理・霊園の区画・霊園の設備・霊園の管理・霊園の区画・霊園の設備・霊園の管理・霊園の区画・霊園の設備・霊園の管理・霊園の区画・霊園の設備・霊園の管理。</p>
      <p>霊園の区画・霊園の設備・霊園の管理・霊園の区画・霊園の設備・霊園の管理・霊園の区画・霊園の設備・霊園の管理・霊園の区画・霊園の設備。</p>
    </section>

    <section class="panel">
      <h2 class="h2">トピックス</h2>
      <div class="topic"><span>2014.7.7</span><span>ホームページを開設しました</span></div>
    </section>
  </main>

  <aside class="side">
    <div class="side-box">
      <div class="side-h">お知らせ</div>
      <ul class="side-list"><li>7月の見学会のお知らせ</li><li>お盆期間の開園時間</li><li>新区画の販売開始</li></ul>
    </div>
    <div class="side-box">
      <div class="side-h">周辺風景</div>
      <div class="scene"><div class="thumb" role="img" aria-label="霊園周辺の風景写真"></div>周辺の景色</div>
      <div class="scene"><div class="thumb" role="img" aria-label="霊園周辺の風景写真"></div>周辺の景色</div>
      <div class="scene"><div class="thumb" role="img" aria-label="霊園周辺の風景写真"></div>周辺の景色</div>
      <div class="scene"><div class="thumb" role="img" aria-label="霊園周辺の風景写真"></div>周辺の景色</div>
    </div>
    <div class="side-box">
      <div class="side-h">アクセス</div>
      <div class="access-photo" role="img" aria-label="霊園入口と管理事務所の写真"></div>
      <p class="access-text">朝日台駅よりバスで約10分。駐車場も完備しておりますので、お車でのご来園も安心です。</p>
      <div class="map" role="img" aria-label="霊園周辺の地図">
        <svg style="position:absolute;left:110px;top:30px" width="24" height="32" viewBox="0 0 24 32"><path d="M12 0a12 12 0 0 1 12 12c0 9-12 20-12 20S0 21 0 12A12 12 0 0 1 12 0z" fill="#c0392b"/><circle cx="12" cy="12" r="4" fill="#fff"/></svg>
      </div>
      <p class="access-text">朝日台霊園<br>〒000-0000 朝日台1-2-3<br>TEL 0120-48-2631</p>
    </div>
  </aside>
</div>

<footer class="footer">
  <div>
    <div class="brand"><div class="brand-mark"></div><div class="brand-name">朝日台霊園</div></div>
    <p class="f-addr">〒000-0000 朝日台1-2-3<br>TEL 0120-48-2631<br>http://www.asahidaireien.jp/</p>
  </div>
  <div class="f-links">ホーム｜朝日台霊園の紹介｜墓所・サイズ｜墓地マップ｜お申込みの方｜資料請求｜お問合せ</div>
  <div class="copy">Copyright © 朝日台霊園 All Rights Reserved.</div>
</footer>
</body>
</html>
```